Business card: GREEN HERONS TRADE SUPPLY

Hello,

This is your mission:

-I've just done my logo on the website. Now, I need A BUSINESS CARD.
-2 same business cards for 2 persons
-Landscape
-Dimension of the business card: 8.5 cm long and 5 cm high
-Different front and back
-For your information: this new company is selling products (fashion accessories, electronics, watches, fragrances, sunglasses, etc. to large clients related to shops in airlines (inflight catalogue), airports, cruises, etc.
-Colors and logo: please use the same colors of the logo attached (in blue with orange details) and follow the spirit of the existing logo.

-Front:
-1st person:
GREEN HERONS s.p.r.l.
Travel Retail Agency
www.greenheronsco.example
Lucien MARTOLIER
Partner
Mobile: +32480627315
Email: lm@greenheronsco.example
-2nd person:
GREEN HERONS s.p.r.l.
Travel Retail Agency
www.greenheronsco.example
Joris VANDERHOLME
Partner
Mobile: +32486153702
Email: jv@greenheronsco.example

-Back
Logo
see attached file. Please use the colors of the logo in blue with orange details.

Reason: I increase time necause i don t know if the deadline is in usa time or european time. I will make the selection at 9pm belgian time.

I'm selling products to large accounts/clients. Some of them do more than 2 Billion eur turnover

Airlines

Must have
• Use the logo.
The buyers get so many business cards.
They should remember me easily.
This is why my logo/company name is a stork and a color. 2 things that people usually remember easily.

```html
<!DOCTYPE html>
<html lang="en">
<head>
<meta charset="utf-8">
<title>Green Herons Trade Supply – Business Card</title>
<link rel="stylesheet" href="https://fonts.googleapis.com/css2?family=Exo+2:wght@400;500&display=swap">
<style>
  :root {
    --page: #d6d7d9;
    --card: #111416;
    --card-shade: #1b1f22;
    --blue: #0a4f94;
    --blue-mid: #1a6fc0;
    --cyan: #1fa0d0;
    --orange: #f07d1e;
    --white: #f2f4f6;
  }
  html, body {
    margin: 0;
    width: 1200px;
    height: 900px;
    overflow: hidden;
    background: var(--page);
    font-family: "Exo 2", sans-serif;
  }
  .sheet {
    position: relative;
    width: 1200px;
    height: 900px;
  }
  .card {
    position: absolute;
    left: 300px;
    width: 600px;
    height: 353px;
    background: var(--card);
    overflow: hidden;
    box-shadow: 0 6px 18px rgba(0,0,0,.28);
  }
  .card--back { top: 70px; }
  .card--front { top: 477px; }
  .card__shade {
    position: absolute;
    inset: 0;
    width: 100%;
    height: 100%;
  }
  .card__decor {
    position: absolute;
    inset: 0;
    width: 100%;
    height: 100%;
  }
  .brand {
    position: absolute;
    margin: 0;
    color: var(--white);
    font-weight: 500;
    line-height: 1.15;
  }
  .card--back .brand {
    left: 270px;
    top: 128px;
    font-size: 36px;
  }
  .card--front .brand {
    left: 60px;
    top: 135px;
    font-size: 24px;
  }
  .contact {
    position: absolute;
    left: 330px;
    top: 48px;
    color: var(--white);
    font-size: 14px;
    line-height: 1.3;
  }
  .contact__name {
    color: var(--blue-mid);
    font-size: 19px;
    font-weight: 500;
    margin: 0 0 14px;
  }
  .contact__line { margin: 0; }
  .contact__label { color: var(--orange); }
  .contact__web { color: var(--orange); margin: 0 0 22px; }
  .contact__company { margin: 0; }
  .contact__company b { color: var(--blue-mid); font-weight: 400; }
</style>
</head>
<body>
<main class="sheet">

  <section class="card card--back" aria-label="Card back">
    <svg class="card__shade" viewBox="0 0 600 353" aria-hidden="true">
      <polygon points="230,0 420,0 280,160 160,160" fill="var(--card-shade)"/>
      <polygon points="330,200 560,200 470,353 250,353" fill="var(--card-shade)"/>
    </svg>
    <svg class="card__decor" viewBox="0 0 600 353" role="img" aria-label="Diagonal band decoration in blue, cyan and orange">
      <defs>
        <linearGradient id="back-decor" x1="0" y1="0" x2="1" y2="1">
          <stop offset="0" stop-color="var(--cyan)"/>
          <stop offset="1" stop-color="var(--blue)"/>
        </linearGradient>
      </defs>
      <polygon points="0,0 205,0 45,353 0,353" fill="url(#back-decor)"/>
    </svg>
    <p class="brand">Green Herons<br>Trade Supply</p>
  </section>

  <section class="card card--front" aria-label="Card front">
    <svg class="card__shade" viewBox="0 0 600 353" aria-hidden="true">
      <polygon points="0,70 260,40 600,0 600,60 250,120 0,150" fill="var(--card-shade)"/>
    </svg>
    <svg class="card__decor" viewBox="0 0 600 353" role="img" aria-label="Lower band decoration in blue and cyan">
      <defs>
        <linearGradient id="front-decor" x1="0" y1="1" x2="1" y2="0">
          <stop offset="0" stop-color="var(--cyan)"/>
          <stop offset="1" stop-color="var(--blue)"/>
        </linearGradient>
      </defs>
      <polygon points="0,272 345,298 230,353 0,353" fill="url(#front-decor)"/>
    </svg>
    <p class="brand">Green Herons<br>Trade Supply</p>
    <div class="contact">
      <p class="contact__name">Joris VANDERHOLME</p>
      <p class="contact__line"><span class="contact__label">M:</span> +32486153702</p>
      <p class="contact__line"><span class="contact__label">E:</span> jv@greenheronsco.example</p>
      <p class="contact__web">www.greenheronsco.example</p>
      <p class="contact__company"><b>GREEN HERONS</b> s.p.r.l.</p>
      <p class="contact__company">Travel Retail Agency</p>
    </div>
  </section>

</main>
</body>
</html>
```